Quillrun Couriers Web design

Take a look at our existing website(www.qlnrun.com) and design a new one, plus coding and recreate an existing logo.

```html
<!DOCTYPE html>
<html lang="en">
<head>
<meta charset="utf-8">
<title>Quillrun Couriers</title>
<link href="https://fonts.googleapis.com/css2?family=Oswald:wght@500;600&family=Poppins:wght@600;700&family=Open+Sans:wght@400;600&display=swap" rel="stylesheet">
<style>
:root{
  --red:#e02210;
  --dark:#2b2b37;
  --darker:#24242f;
  --ink:#1d1d24;
  --muted:#777;
  --blue:#4a7fc9;
  --field:#616170;
}
*{box-sizing:border-box;margin:0;padding:0}
html,body{width:1200px;height:3378px;overflow:hidden}
body{font-family:"Open Sans",sans-serif;color:var(--ink);background:#fff;position:relative}
.abs{position:absolute}
/* top bar */
.topbar{top:0;left:0;width:1200px;height:37px;background:var(--dark)}
.topbar .red{position:absolute;left:197px;right:0;top:0;height:37px;background:var(--red);clip-path:polygon(16px 0,100% 0,100% 100%,0 100%)}
.topbar .item{position:absolute;top:10px;color:#fff;font-size:13px;display:flex;align-items:center;gap:8px}
.topbar .soc{position:absolute;top:12px;display:flex;gap:13px}
.topbar .soc i{width:12px;height:12px;border-radius:2px;background:#fff;display:block}
.search{position:absolute;top:10px;left:1040px;color:#fff;font-size:13px;font-weight:600}
/* header */
.header{top:37px;left:0;width:1200px;height:100px;background:var(--dark)}
.logo{position:absolute;left:40px;top:30px;display:flex;align-items:center;gap:10px;color:#fff;font-family:"Oswald",sans-serif;font-weight:600;font-size:34px}
.logo i{width:16px;height:16px;background:#fff;display:block}
.nav{position:absolute;left:325px;top:42px;display:flex;font-family:"Oswald",sans-serif;font-weight:500;font-size:13px;color:#fff}
.nav span{padding:0 19px;border-right:1px solid #55556a;line-height:16px}
.nav span:last-child{border:none}
.nav .on{color:var(--red)}
.quote-btn{position:absolute;left:1028px;top:33px;width:127px;height:34px;border-radius:17px;background:#4a4a58;color:#fff;font-family:"Oswald",sans-serif;font-size:13px;text-align:center;line-height:34px}
/* hero */
.hero{top:137px;left:0;width:1200px;height:681px;background:linear-gradient(100deg,#c27a4a 0%,#5a4c55 30%,#3d4a5e 55%,#2a3040 100%)}
.hero-frame{position:absolute;left:92px;top:175px;width:242px;height:288px;border:8px solid var(--red);border-right:none;clip-path:polygon(0 0,100% 0,100% 12px,8px 12px,8px 276px,100% 276px,100% 100%,0 100%)}
.hero-frame2{position:absolute;left:92px;top:175px;width:242px;height:288px}
.hero-frame2 b{position:absolute;right:0;width:8px;height:54px;background:var(--red)}
.hero h1{position:absolute;left:161px;top:212px;color:#fff;font-family:"Poppins",sans-serif;font-weight:700;font-size:64px;line-height:64px;letter-spacing:1px}
.hero h2{position:absolute;left:161px;top:272px;color:#fff;font-family:"Poppins",sans-serif;font-weight:700;font-size:50px;line-height:56px}
.book{position:absolute;left:268px;top:342px;width:110px;height:34px;border-radius:17px;background:var(--red);color:#fff;font-size:11px;font-weight:700;text-align:center;line-height:34px}
/* about */
.tag{color:var(--red);font-size:13px}
.about-tag{top:947px;left:74px}
.about h3{position:absolute;left:70px;top:970px;font-family:"Poppins",sans-serif;font-weight:700;font-size:42px;line-height:52px;color:var(--ink)}
.about h4{position:absolute;left:70px;top:1019px;font-family:"Poppins",sans-serif;font-weight:700;font-size:30px;color:var(--ink)}
.about p{position:absolute;left:72px;top:1078px;width:500px;font-size:12.5px;line-height:25px;color:var(--muted);text-align:justify}
.van{top:898px;left:627px;width:514px;height:361px;background:radial-gradient(ellipse at center,#dcdcdc 0%,#eeeeee 55%,#fff 75%)}
.feat{position:absolute;top:1322px;display:flex;gap:20px}
.feat svg{flex:none}
.feat b{display:block;font-family:"Poppins",sans-serif;font-size:13px;letter-spacing:1px;color:var(--ink)}
.feat span{font-size:13.5px;color:#999;letter-spacing:.5px}
.rule{top:1435px;left:32px;width:1135px;height:1px;background:#e5e5e5}
.rule-blue{top:1433px;left:214px;width:849px;height:4px;background:var(--blue)}
/* services */
.svc-tag{top:1554px;left:0;width:1200px;text-align:center;color:var(--red);font-size:12px;font-weight:700}
.svc-h{top:1590px;left:0;width:1200px;text-align:center;font-family:"Poppins",sans-serif;font-weight:700;font-size:37px;line-height:44px;color:var(--ink)}
.card{position:absolute;top:1731px;width:330px;height:426px;background:#fff;box-shadow:0 6px 20px rgba(0,0,0,.08)}
.card .photo{height:267px;position:relative}
.card .box{position:absolute;left:20px;top:17px;width:292px;height:232px;background:var(--darker);color:#fff;display:flex;flex-direction:column;align-items:center;justify-content:center;gap:20px;font-family:"Poppins",sans-serif;font-weight:600;font-size:16px}
.card .desc{height:104px;margin:0 26px;border-bottom:1px solid #eee;padding-top:22px;text-align:center;font-size:13px;line-height:21px;color:#666}
.card .more{text-align:center;font-size:12px;font-weight:700;padding-top:20px;color:var(--ink)}
.card.active{background:var(--dark)}
.card.active .photo{background:linear-gradient(135deg,#3a3a48,#2b2b37)}
.card.active .desc{color:#fff;border:none}
.card.active .more{background:var(--red);color:#fff;height:50px;padding-top:18px;margin-top:5px}
/* quote */
.quote{top:2253px;left:2px;width:1198px;height:586px;background:var(--dark)}
.quote .photo{position:absolute;left:0;top:0;width:584px;height:586px;clip-path:polygon(0 0,334px 0,584px 100%,0 100%);background:linear-gradient(180deg,#f4f4f4 0%,#e6e6e6 60%,#d2d2d2 100%)}
.q-title{position:absolute;left:716px;top:80px;color:#fff;font-family:"Oswald",sans-serif;font-weight:600;font-size:22px;letter-spacing:1px}
.q-title em{color:var(--red);font-style:normal;margin:0 18px}
.q-text{position:absolute;left:612px;top:147px;width:498px;text-align:center;color:#bbb;font-size:12.5px;line-height:20px}
.field{position:absolute;background:var(--field);color:#fff;font-size:12px;padding:18px 21px}
.send{position:absolute;left:775px;top:462px;width:107px;height:44px;background:var(--red);color:#fff;font-family:"Oswald",sans-serif;font-size:12px;text-align:center;line-height:44px}
/* footer */
.footer{top:2990px;left:0;width:1200px;height:388px;background:var(--dark)}
.addr{top:2902px;left:206px;width:783px;height:117px;background:var(--red);display:flex}
.addr .col{flex:1;display:flex;align-items:center;gap:22px;padding-left:57px;color:#fff}
.addr .col:first-child{border-right:1px solid rgba(255,255,255,.3);margin:18px 0;padding-left:57px}
.addr .ico{width:58px;height:58px;border:2px solid #fff;display:flex;align-items:center;justify-content:center}
.addr h5{font-family:"Oswald",sans-serif;font-weight:500;font-size:21px;margin-bottom:4px}
.addr p{font-size:12.5px;line-height:21px}
.fhead{position:absolute;top:3072px;height:42px;width:320px;border-bottom:1px solid #3e3e4c}
.fhead span{display:inline-block;background:var(--red);color:#fff;font-family:"Oswald",sans-serif;font-weight:600;font-size:16px;letter-spacing:.5px;padding:0 42px 0 18px;line-height:42px;clip-path:polygon(0 0,82% 0,100% 100%,0 100%)}
.flogo{position:absolute;left:93px;top:3172px;display:flex;align-items:center;gap:10px;color:#fff;font-family:"Oswald",sans-serif;font-weight:600;font-size:38px}
.flogo i{width:18px;height:18px;background:#fff;display:block}
.fsoc{position:absolute;left:93px;top:3244px;display:flex;gap:24px}
.fsoc i{width:15px;height:15px;border-radius:50%;background:#aaa;display:block}
.links{position:absolute;top:3155px;font-size:13.5px;color:#bbb;line-height:28.5px}
.links div::before{content:"→";margin-right:12px;color:#999}
.contact{position:absolute;left:785px;top:3155px;font-size:13.5px;color:#ccc;line-height:28.5px}
.contact div{display:flex;align-items:center;gap:18px}
.contact i{width:13px;height:13px;background:#aaa;border-radius:2px;display:block}
.bottom{top:3298px;left:0;width:1200px;height:80px;background:var(--darker)}
.bottom .red{position:absolute;left:0;top:0;width:462px;height:80px;background:var(--red);clip-path:polygon(0 0,428px 0,100% 100%,0 100%)}
.bottom .pw{position:absolute;left:93px;top:32px;color:#fff;font-size:12px}
.bottom .cp{position:absolute;left:920px;top:32px;color:#bbb;font-size:12px}
.bottom .up{position:absolute;left:1153px;top:32px;color:#fff;font-size:11px}
</style>
</head>
<body>

<div class="abs topbar">
  <div class="red"></div>
  <div class="item" style="left:238px">
    <svg width="13" height="13" viewBox="0 0 24 24"><path fill="#fff" d="M6.6 10.8a15 15 0 006.6 6.6l2.2-2.2c.3-.3.7-.4 1-.2 1.1.4 2.3.6 3.6.6.6 0 1 .4 1 1V20c0 .6-.4 1-1 1A17 17 0 013 4c0-.6.4-1 1-1h3.5c.6 0 1 .4 1 1 0 1.3.2 2.5.6 3.6.1.3 0 .7-.2 1z"/></svg>
    (+61) 300 55 0142
  </div>
  <div class="item" style="left:398px">
    <svg width="14" height="11" viewBox="0 0 14 11"><rect width="14" height="11" fill="#fff"/><path d="M0 0l7 6 7-6" stroke="#e02210" fill="none"/></svg>
    (info@example.com
  </div>
  <div class="soc" style="left:898px"><i></i><i></i><i></i><i></i></div>
  <div class="abs" style="left:1023px;top:8px;width:1px;height:20px;background:rgba(255,255,255,.4)"></div>
  <div class="search">Search...</div>
  <svg class="abs" style="left:1133px;top:10px" width="16" height="16" viewBox="0 0 16 16"><circle cx="6.5" cy="6.5" r="5" stroke="#fff" stroke-width="2" fill="none"/><path d="M10 10l5 5" stroke="#fff" stroke-width="2"/></svg>
</div>

<div class="abs header">
  <div class="logo"><i></i>Quillrun</div>
  <nav class="nav">
    <span class="on">HOME</span><span>ABOUT US</span><span>SERVICES</span><span>RATES</span><span>CUSTOMER BENEFITS</span><span>LOGISTICS</span><span>CONTACT US</span><span></span>
  </nav>
  <div class="quote-btn">GET A QUOTE</div>
</div>

<section class="abs hero" role="img" aria-label="Truck on a road beside a container port at dusk with a plane overhead">
  <div class="hero-frame"></div>
  <div class="hero-frame2"><b style="top:0"></b><b style="bottom:0"></b></div>
  <h1>DELIVERING</h1>
  <h2>service on time</h2>
  <div class="book">BOOK NOW</div>
</section>

<section class="about">
  <div class="abs tag about-tag">{ WHO WE ARE }</div>
  <h3>Committed To Providing</h3>
  <h4>Professional Messenger Services</h4>
  <p>Welcome to Quillrun Couriers. We are committed to providing professional messenger services to cater for the most important, emergency and time sensitive deliveries valuable to your company. Our services range from scheduled local and long distance, same day to all types of On Demand services. Our goal is to become a leader by showing reliability, integrity as well as competitive pricing.<br>Our company is licensed, bonded and fully insured with commercial grade insurance. Our personnel are professional, uniformed and vehicles are identified and all have commercial insurance. ...</p>
  <div class="abs van" role="img" aria-label="White branded delivery van"></div>

  <div class="feat" style="left:78px">
    <svg width="34" height="50" viewBox="0 0 34 50"><path d="M17 2c8 8 8 22 5 34H12C9 24 9 10 17 2zM12 36l-6 8 6-3M22 36l6 8-6-3M17 38v10" stroke="#ccc" stroke-width="1.5" fill="none"/></svg>
    <div><b>FAST DELIVERY</b><span>unde omnis iste natus error</span></div>
  </div>
  <div class="feat" style="left:380px">
    <svg width="36" height="42" viewBox="0 0 36 42"><path d="M18 2l15 6v12c0 10-7 17-15 20C10 37 3 30 3 20V8z" stroke="#ccc" stroke-width="1.5" fill="none"/><path d="M11 20l6 6 9-11" stroke="#ccc" stroke-width="1.5" fill="none"/></svg>
    <div><b>SECURED SERVICE</b><span>unde omnis iste natus error sit voluptatem</span></div>
  </div>
  <div class="feat" style="left:792px">
    <svg width="36" height="46" viewBox="0 0 36 46"><rect x="4" y="2" width="28" height="40" rx="3" stroke="#ccc" stroke-width="1.5" fill="none"/><path d="M4 14h28M4 30h28M10 42v3M26 42v3" stroke="#ccc" stroke-width="1.5"/></svg>
    <div><b>WORLD WIDE SHIPPING</b><span>unde omnis iste natus error sit</span></div>
  </div>
</section>
<div class="abs rule"></div>
<div class="abs rule-blue"></div>

<div class="abs svc-tag">&lsaquo;&nbsp; OUR SERVICES &nbsp;&rsaquo;</div>
<h2 class="abs svc-h">Moving Your Products Across<br>All Borders</h2>

<div class="card" style="left:89px">
  <div class="photo" role="img" aria-label="Doctor with stethoscope" style="background:linear-gradient(135deg,#dfe7f2,#4a74b0)">
    <div class="box">
      <svg width="54" height="66" viewBox="0 0 54 66"><path d="M6 4v16a13 13 0 0026 0V4M19 33v14a12 12 0 0024 0v-8" stroke="#e02210" stroke-width="4" fill="none"/><circle cx="43" cy="34" r="6" stroke="#e02210" stroke-width="4" fill="none"/></svg>
      Hospital &amp; Medical Care
    </div>
  </div>
  <div class="desc">Hospital &amp; Medical Care , Home Deliveries, Pharmaceuticals and Critical Routes...</div>
  <div class="more"><span style="color:var(--red)">&#8600;</span> MORE DETAILS</div>
</div>

<div class="card active" style="left:446px">
  <div class="photo" role="img" aria-label="Documents and calculator on a desk">
    <div class="box" style="background:transparent;top:40px">
      <svg width="62" height="62" viewBox="0 0 62 62"><path d="M31 2L2 18h58z" fill="#e02210"/><rect x="4" y="22" width="54" height="4" fill="#e02210"/><rect x="9" y="30" width="7" height="20" fill="#e02210"/><rect x="21" y="30" width="7" height="20" fill="#e02210"/><rect x="34" y="30" width="7" height="20" fill="#e02210"/><rect x="46" y="30" width="7" height="20" fill="#e02210"/><rect x="2" y="54" width="58" height="6" fill="#e02210"/><circle cx="31" cy="12" r="4" fill="#fff"/></svg>
      Banking &amp; Brokerage
    </div>
  </div>
  <div class="desc">Banking &amp; Brokerage, Emergency Deliveries, Mortgage Documents, Interoffice Routes ...</div>
  <div class="more">MORE DETAILS</div>
</div>

<div class="card" style="left:801px">
  <div class="photo" role="img" aria-label="Judge gavel on a wooden desk" style="background:linear-gradient(135deg,#e0782a,#5a1c0c)">
    <div class="box">
      <svg width="66" height="54" viewBox="0 0 66 54"><rect x="16" y="6" width="22" height="12" transform="rotate(35 27 12)" fill="#e02210"/><rect x="30" y="20" width="30" height="6" transform="rotate(35 30 20)" fill="#e02210"/><rect x="4" y="40" width="36" height="6" fill="#e02210"/><rect x="0" y="47" width="44" height="6" fill="#e02210"/></svg>
      Legal Filings
    </div>
  </div>
  <div class="desc">Legal, Administrative and also deliveries associated with Manufacturing. ...</div>
  <div class="more"><span style="color:var(--red)">&#8600;</span> MORE DETAILS</div>
</div>

<section class="abs quote">
  <div class="photo" role="img" aria-label="Forklift loading boxes into a shipping container"></div>
  <div class="q-title"><em>\\</em>REQUEST A QUICK QUOTE<em>\\</em></div>
  <p class="q-text">We love to listen and we are eagerly waiting to talk to you regarding your project. Get in touch with us if you have any queries and we will get back to you as soon as possible.</p>
  <div class="field" style="left:613px;top:238px;width:242px;height:50px">Your name here</div>
  <div class="field" style="left:864px;top:238px;width:242px;height:50px">Subject</div>
  <div class="field" style="left:613px;top:297px;width:242px;height:50px">Your email</div>
  <div class="field" style="left:864px;top:297px;width:242px;height:50px">Phone</div>
  <div class="field" style="left:613px;top:356px;width:493px;height:97px;font-family:monospace;font-size:11px">Your message</div>
  <div class="send">SEND MESSAGE</div>
</section>

<footer class="abs footer"></footer>
<div class="abs addr">
  <div class="col">
    <div class="ico"><svg width="28" height="28" viewBox="0 0 28 28"><path d="M26 2L2 12l11 3 3 11z" fill="#fff"/></svg></div>
    <div><h5>Head Office</h5><p>Quillrun Couriers<br>512 Harbor Lane, Lakeview, NY 14000</p></div>
  </div>
  <div class="col">
    <div class="ico"><svg width="28" height="28" viewBox="0 0 28 28"><path d="M26 2L2 12l11 3 3 11z" fill="#fff"/></svg></div>
    <div><h5>Mailing Address</h5><p>Quillrun Couriers<br>P.O. Box 1180, Fairport, NY 14450</p></div>
  </div>
</div>

<div class="fhead" style="left:93px"><span>ABOUT US</span></div>
<div class="fhead" style="left:439px"><span>INFORMATION</span></div>
<div class="fhead" style="left:785px"><span>TRANSPORT OFFICE</span></div>

<div class="flogo"><i></i>Quillrun</div>
<div class="fsoc"><i></i><i></i><i></i><i></i><i></i><i></i></div>

<div class="links" style="left:439px"><div>Home</div><div>About Us</div><div>Services</div><div>Rates</div></div>
<div class="links" style="left:572px"><div>Customer Benefits</div><div>Logistics</div><div>Contact</div></div>
<div class="contact">
  <div><i></i>555-010-7170,&nbsp; 555-010-2427</div>
  <div><i></i>info@qlnrun.com</div>
  <div><i></i>555-010-7041</div>
  <div><i style="border-radius:50%"></i><span style="font-size:12px">Mon - Sat: 9:00 - 18:00</span></div>
</div>

<div class="abs bottom">
  <div class="red"></div>
  <div class="pw">Powered By Northgrid Studio...</div>
  <div class="cp">© 2011 Quillrun Couriers</div>
  <div class="up">&#9650;</div>
</div>

</body>
</html>
```